Need an event poster for an automotive event.
The event is a half mile trap speed event. Sometimes called a VelMark event, they have a 1/2 mile to see how fast They can go. They run one car at a time, it is not a side-by-side race.
Title of the event is “KRBO Sidevalve Autumn Classic”. Dates are October 3-4 2020. Location Blytheville Arkansas. Website is KRBOmile.com. Most participants will be 50 and older .
All entries must be a carbureted flathead engine .

```html
<!DOCTYPE html>
<html lang="en">
<head>
<meta charset="utf-8">
<title>KRBO Sidevalve Autumn Classic</title>
<link rel="stylesheet" href="https://fonts.googleapis.com/css2?family=Anton&family=Montserrat:wght@800&family=Open+Sans:wght@600;700;800&display=swap">
<style>
  :root {
    --paper: #ffffff;
    --slate: #3c4759;
    --royal: #1034f5;
    --signal-red: #f5132b;
    --ink: #000000;
    --white: #ffffff;
  }
  html, body {
    margin: 0;
    padding: 0;
    overflow: hidden;
    background: var(--paper);
  }
  .poster {
    position: relative;
    width: 900px;
    height: 1200px;
    overflow: hidden;
    background: var(--paper);
    font-family: "Open Sans", Arial, sans-serif;
  }
  .brand-mark {
    position: absolute;
    left: 28px;
    top: 201px;
    width: 400px;
    text-align: center;
    font-family: "Open Sans", Arial, sans-serif;
    font-weight: 700;
    font-size: 118px;
    line-height: 118px;
    letter-spacing: 4px;
    color: var(--slate);
  }
  .title-divider {
    position: absolute;
    left: 441px;
    top: 49px;
    height: 236px;
    border-left: 3px dotted var(--slate);
  }
  .event-title {
    position: absolute;
    left: 0;
    top: 0;
    width: 900px;
    height: 300px;
  }
  .event-title text {
    font-family: "Anton", Impact, sans-serif;
    font-size: 90px;
    fill: var(--slate);
  }
  .rules-panel {
    position: absolute;
    left: 0;
    top: 363px;
    width: 410px;
    height: 478px;
    background: var(--royal);
  }
  .rules-text {
    position: absolute;
    left: 24px;
    top: 394px;
    width: 370px;
    margin: 0;
    color: var(--white);
    font-weight: 600;
    font-size: 45px;
    line-height: 52px;
  }
  .rules-text p { margin: 0 0 24px; }
  .action-photo {
    position: absolute;
    left: 0;
    top: 0;
    width: 900px;
    height: 1200px;
  }
  .event-date {
    position: absolute;
    left: 0;
    top: 912px;
    width: 900px;
    margin: 0;
    text-align: center;
    font-family: "Montserrat", Arial, sans-serif;
    font-weight: 800;
    font-size: 68px;
    line-height: 80px;
    color: var(--ink);
  }
  .event-location {
    position: absolute;
    left: 0;
    top: 992px;
    width: 900px;
    margin: 0;
    text-align: center;
    font-weight: 700;
    font-size: 52px;
    line-height: 60px;
    color: var(--ink);
  }
  .web-band {
    position: absolute;
    left: 0;
    top: 1071px;
    width: 900px;
    height: 129px;
    background: var(--signal-red);
  }
  .web-address {
    position: absolute;
    left: 0;
    top: 1079px;
    width: 900px;
    margin: 0;
    text-align: center;
    color: var(--white);
    font-weight: 800;
    font-size: 78px;
    line-height: 114px;
  }
</style>
</head>
<body>
<main class="poster">
  <div class="brand-mark">KRBO</div>
  <div class="title-divider"></div>
  <svg class="event-title" viewBox="0 0 900 300" width="900" height="300" role="heading" aria-level="1" aria-label="KRBO Sidevalve Autumn Classic">
    <text x="460" y="114">KRBO</text>
    <text x="460" y="201">Sidevalve</text>
    <text x="460" y="285" textLength="420" lengthAdjust="spacingAndGlyphs">Autumn Classic</text>
  </svg>

  <div class="rules-panel"></div>

  <svg class="action-photo" viewBox="0 0 900 1200" width="900" height="1200">
    <defs>
      <linearGradient id="track-tones" x1="0" y1="0" x2="0" y2="1">
        <stop offset="0" stop-color="#8f8a83"/>
        <stop offset="0.25" stop-color="#9c9a8c"/>
        <stop offset="0.42" stop-color="#6f9a4f"/>
        <stop offset="0.6" stop-color="#7c8f86"/>
        <stop offset="0.78" stop-color="#c2c4c8"/>
        <stop offset="1" stop-color="#d8d9dc"/>
      </linearGradient>
    </defs>
    <polygon points="407,346 904,386 886,907 364,864" fill="#9a9a9a" opacity="0.45"/>
    <polygon points="403,342 900,382 882,903 360,860" fill="url(#track-tones)"
      role="img" aria-label="Photo of a rider on a blue and white sport motorcycle at speed on the track"/>
  </svg>

  <div class="rules-text">
    <p>Most<br>participants will<br>be 50 and older.</p>
    <p>All entries must<br>be a carbureted<br>flathead<br>engine.</p>
  </div>

  <p class="event-date">October 3-4 2020</p>
  <p class="event-location">Location: Blytheville Arkansas</p>

  <div class="web-band"></div>
  <p class="web-address">KRBOmile.com</p>
</main>
</body>
</html>
```